Web Design Project

Dear designer(s),

I need a design for a shop who's specialized into...

-Material to fix or do tailor made clothing (cloth, buttons, zippers etc)
-Curtains (static/pull-up)
-Blinds (plastic/wood)

that kind of stuff.

Good thing is that I can provide a lot of pretty photo's to work with. I have 3.5 Gigabyte of 300-1200 dpi photo's altho I converted most of them to 72dpi for your convenience (75Mb).

You can download the working material from this quellbin link:

http://files.quellbin.net/u/31920586/Velunor.zip

this is an updated file, it contains the dutch menu items to use in your design

http://files.quellbin.net/u/31920586/Velunor_Content.txt

Notice: take your time to come up with something nice. I prefer 1 or 2 designs from a designer that has been thinked of, than 5 quick ones.
Updates

Thank you for those who posted designs already but I want to clarify something.

As I mentioned it's a shop, that's a physical shop and not a webshop.

So you can safe some time and skip drawing the shopping cart icons, shop items on the homepage and other shop related things.

They don't want to start online reselling as they already spend most of their time in their shop to catch up with all orders.

Keep up the good work!

Industry/Entity Type

Clothing

Requirements
Nice to have
• Maybe the hi-res pictures can be used as background ratotor that appears left/right next to the centered website content?

Since there is a lot of material each section might have his topic linked set of thumbnails that opens a bigger image on clicking?

```html
<!DOCTYPE html>
<html lang="en">
<head>
<meta charset="utf-8">
<title>Velunor – Home</title>
<link href="https://fonts.googleapis.com/css2?family=Open+Sans:wght@400;600;700&family=Noto+Serif:wght@400&display=swap" rel="stylesheet">
<style>
:root{
  --blue:#1f7fc4;
  --ink:#333;
  --muted:#888;
  --line:#e2e2e2;
  --bar:#efefef;
  --band:#e6e6e6;
  --white:#fff;
  --dark:#3a3a3a;
}
*{box-sizing:border-box;margin:0;padding:0}
html,body{width:882px;height:1200px;overflow:hidden}
body{background:var(--white);font-family:"Open Sans",Arial,sans-serif;color:var(--ink);font-size:10px;position:relative}
.wrap{position:absolute;left:35px;width:812px}

/* header */
.header{top:0;height:88px}
.brand{position:absolute;left:0;top:26px;display:flex;align-items:center;gap:8px}
.brand-mark{width:20px;height:20px;background:var(--blue)}
.brand-name{font-size:24px;font-weight:600;color:var(--blue);letter-spacing:.5px;line-height:28px}
.brand-tag{position:absolute;left:28px;top:56px;font-size:8px;color:var(--muted);white-space:nowrap}
.hours-line{position:absolute;right:0;top:22px;font-size:9px;color:var(--ink);white-space:nowrap}
.top-links{position:absolute;right:0;top:42px;display:flex;gap:16px;font-size:9px;color:var(--ink);white-space:nowrap}

/* nav */
.nav{top:88px;height:29px;background:var(--bar);border-top:1px solid var(--line);border-bottom:1px solid var(--line);display:flex;align-items:center}
.nav a{padding:0 14px;font-size:10px;color:#555;line-height:27px;white-space:nowrap}
.nav a.active{color:var(--blue);font-weight:600}

/* hero */
.hero{top:117px;height:377px;background:linear-gradient(180deg,#dfe6ea 0%,#f4f5f3 45%,#d8d6d1 75%,#b9b4ad 100%)}
.hero-arrow{position:absolute;top:168px;width:26px;height:40px;background:rgba(255,255,255,.8);display:flex;align-items:center;justify-content:center}
.hero-arrow.prev{left:0}
.hero-arrow.next{right:0}

/* promos */
.promo{position:absolute;top:514px;height:70px;color:var(--white);overflow:hidden}
.promo-custom{left:80px;width:235px;background:linear-gradient(135deg,#d7d3cc,#a9a49c)}
.promo-sale{left:323px;width:236px;background:linear-gradient(90deg,#c7b79a,#e4d9c2 50%,#a48b5e)}
.promo-fabrics{left:573px;width:227px;background:linear-gradient(135deg,#c8a862,#e6d4a4 60%,#b8924a)}
.promo-custom .t1{position:absolute;left:14px;top:10px;font-size:14px;color:#444;line-height:16px}
.promo-custom .t2{position:absolute;left:14px;top:25px;font-size:20px;color:#555;font-weight:600;line-height:24px}
.promo-custom .btn{position:absolute;left:14px;top:52px;font-size:7px;line-height:10px;background:var(--dark);color:#fff;padding:0 5px}
.promo-sale .box{position:absolute;right:18px;top:8px;width:96px;height:54px;background:rgba(255,255,255,.92);color:#6c4b22;text-align:center}
.promo-sale .small{font-size:7px;line-height:10px;padding-top:3px}
.promo-sale .big{font-size:22px;font-weight:700;line-height:26px}
.promo-sale .btn{display:inline-block;font-size:7px;line-height:10px;background:#8a6432;color:#fff;padding:0 6px}
.promo-fabrics .t1{position:absolute;left:12px;top:6px;font-size:24px;line-height:30px;font-weight:600;color:#fff}
.promo-fabrics .t2{position:absolute;left:12px;top:39px;font-size:10px;line-height:14px;font-weight:700;background:#fff;color:#9b7a36;padding:0 5px}
.promo-fabrics .t3{position:absolute;left:12px;top:56px;font-size:7px;line-height:10px;color:#fff;white-space:nowrap}

/* collection */
.section-title{top:620px;font-family:"Noto Serif",Georgia,serif;font-weight:400;font-size:13px;color:var(--ink)}
.collection{top:660px;height:222px;display:flex;gap:12px}
.card{width:153px;border:1px solid var(--line);position:relative;text-align:center}
.card-img{height:148px}
.img-a{background:linear-gradient(160deg,#e9eef1,#bfc8cd)}
.img-b{background:linear-gradient(160deg,#d9cfc2,#8c7b68)}
.img-c{background:linear-gradient(160deg,#f0ede7,#c9c1b2)}
.img-d{background:linear-gradient(160deg,#e5ecf0,#a9b9c4)}
.img-e{background:linear-gradient(160deg,#eef1ec,#c6d0bd)}
.overlay{position:absolute;left:0;top:0;width:100%;height:148px;background:rgba(40,40,40,.72);color:#fff;padding:12px 10px;text-align:left}
.overlay .o-title{font-size:9px;font-weight:600;margin-bottom:5px;line-height:12px}
.overlay p{font-size:7px;line-height:10px;color:#ddd}
.overlay .o-btns{position:absolute;left:10px;bottom:10px;display:flex;gap:4px}
.overlay .o-btns span{width:16px;height:16px;background:#fff}
.card-name{font-size:8px;line-height:11px;color:#666;margin-top:8px}
.card-more{font-size:9px;line-height:12px;color:var(--blue);font-weight:600;margin-top:5px}
.card-actions{position:absolute;left:0;bottom:0;width:100%;height:24px;border-top:1px solid var(--line);display:flex;justify-content:space-around;align-items:center;background:#fafafa}

/* service band */
.band{position:absolute;left:0;top:946px;width:882px;height:64px;background:var(--band)}
.band-item{position:absolute;top:18px;display:flex;align-items:center;gap:10px;font-size:10px;line-height:28px;font-weight:600;color:#444;letter-spacing:.3px;white-space:nowrap}
.band-item.made{left:48px}
.band-item.call{left:508px}
.band-icon{width:28px;height:28px;border-radius:50%;background:var(--dark);display:flex;align-items:center;justify-content:center}

/* footer */
.footer{top:1030px;height:140px;display:flex}
.col{width:120px}
.col.visit{width:170px}
.col h4{font-family:"Noto Serif",Georgia,serif;font-weight:400;font-size:11px;line-height:14px;color:var(--ink);margin-bottom:8px}
.col p{font-size:7px;line-height:10px;color:var(--muted);width:140px}
.col ul{list-style:none}
.col li{font-size:7.5px;color:#666;line-height:14px;display:flex;align-items:center;gap:5px;white-space:nowrap}
.col li::before{content:"";width:3px;height:3px;background:var(--blue);border-radius:50%}
.contact li::before{width:6px;height:6px;border-radius:1px}
.copyright{position:absolute;left:0;top:1180px;width:882px;height:20px;border-top:1px solid var(--line);font-size:7px;line-height:10px;color:var(--muted);padding:5px 35px}
</style>
</head>
<body>

<header class="wrap header">
  <div class="brand"><span class="brand-mark"></span><span class="brand-name">Velunor</span></div>
  <div class="brand-tag">Cloth · Curtains · Blinds</div>
  <div class="hours-line">Open Mon – Sat 9:00 – 18:00</div>
  <nav class="top-links"><a>About us</a><a>Services</a><a>Gallery</a><a>Route</a><a>Contact</a></nav>
</header>

<nav class="wrap nav">
  <a class="active">Home</a><a>Cloth</a><a>Fabric</a><a>Table cloth</a><a>Decoration cloth</a><a>Roll systems</a><a>Contact</a>
</nav>

<section class="wrap hero" role="img" aria-label="Bright living room with white sofa, lime chairs and window blinds">
  <div class="hero-arrow prev"><svg width="10" height="14" viewBox="0 0 10 14"><path d="M8 1 2 7l6 6" fill="none" stroke="#666" stroke-width="2"/></svg></div>
  <div class="hero-arrow next"><svg width="10" height="14" viewBox="0 0 10 14"><path d="M2 1l6 6-6 6" fill="none" stroke="#666" stroke-width="2"/></svg></div>
</section>

<div class="promo promo-custom" role="img" aria-label="Tailored curtain detail">
  <div class="t1">Tailor</div><div class="t2">Custom</div><div class="btn">MADE TO MEASURE</div>
</div>
<div class="promo promo-sale" role="img" aria-label="Folded fabrics on display">
  <div class="box"><div class="small">IN STORE</div><div class="big">30% off</div><div class="btn">VISIT US</div></div>
</div>
<div class="promo promo-fabrics" role="img" aria-label="Golden fabric rolls">
  <div class="t1">Fabrics</div><div class="t2">WIDE SELECTION</div><div class="t3">COLOR, STYLE AND PATTERNS ›</div>
</div>

<h3 class="wrap section-title">New Collection</h3>

<section class="wrap collection">
  <article class="card">
    <div class="card-img img-a" role="img" aria-label="Room with white roller blinds"></div>
    <div class="card-name">Lorem ipsum dolor sit amet</div>
    <div class="card-more">View more</div>
    <div class="card-actions"><svg width="10" height="10" viewBox="0 0 10 10"><circle cx="4" cy="4" r="3" fill="none" stroke="#999" stroke-width="1.4"/><path d="M6.5 6.5 9 9" stroke="#999" stroke-width="1.4"/></svg></div>
  </article>
  <article class="card">
    <div class="card-img img-b" role="img" aria-label="Brown curtains in a lounge"></div>
    <div class="overlay">
      <div class="o-title">Lorem ipsum dolor sit amet</div>
      <p>Lorem ipsum dolor sit amet, consectetur adipiscing elit sed do eiusmod tempor.</p>
      <div class="o-btns"><span></span><span></span></div>
    </div>
    <div class="card-name">Lorem ipsum dolor sit amet</div>
    <div class="card-more">View more</div>
    <div class="card-actions"><svg width="10" height="10" viewBox="0 0 10 10"><circle cx="4" cy="4" r="3" fill="none" stroke="#999" stroke-width="1.4"/><path d="M6.5 6.5 9 9" stroke="#999" stroke-width="1.4"/></svg></div>
  </article>
  <article class="card">
    <div class="card-img img-c" role="img" aria-label="Light linen curtains by a window"></div>
    <div class="card-name">Lorem ipsum dolor sit amet</div>
    <div class="card-more">View more</div>
    <div class="card-actions"><svg width="10" height="10" viewBox="0 0 10 10"><circle cx="4" cy="4" r="3" fill="none" stroke="#999" stroke-width="1.4"/><path d="M6.5 6.5 9 9" stroke="#999" stroke-width="1.4"/></svg></div>
  </article>
  <article class="card">
    <div class="card-img img-d" role="img" aria-label="Bedroom with pleated blinds"></div>
    <div class="card-name">Lorem ipsum dolor sit amet</div>
    <div class="card-more">View more</div>
    <div class="card-actions"><svg width="10" height="10" viewBox="0 0 10 10"><circle cx="4" cy="4" r="3" fill="none" stroke="#999" stroke-width="1.4"/><path d="M6.5 6.5 9 9" stroke="#999" stroke-width="1.4"/></svg></div>
  </article>
  <article class="card">
    <div class="card-img img-e" role="img" aria-label="Green roller blind in a kitchen"></div>
    <div class="card-name">Lorem ipsum dolor sit amet</div>
    <div class="card-more">View more</div>
    <div class="card-actions"><svg width="10" height="10" viewBox="0 0 10 10"><circle cx="4" cy="4" r="3" fill="none" stroke="#999" stroke-width="1.4"/><path d="M6.5 6.5 9 9" stroke="#999" stroke-width="1.4"/></svg></div>
  </article>
</section>

<section class="band">
  <div class="band-item made">
    <span class="band-icon"><svg width="14" height="14" viewBox="0 0 14 14"><path d="M2 7.5 5.5 11 12 3" fill="none" stroke="#fff" stroke-width="2"/></svg></span>
    MADE TO MEASURE IN OUR OWN WORKSHOP
  </div>
  <div class="band-item call">
    <span class="band-icon"><svg width="12" height="12" viewBox="0 0 12 12"><path d="M2 1l2 0 1 3-1.5 1a6 6 0 0 0 3.5 3.5L8 7l3 1v2a1 1 0 0 1-1 1A9 9 0 0 1 1 2a1 1 0 0 1 1-1z" fill="#fff"/></svg></span>
    CALL US! TOLL FREE 00 000 0000
  </div>
</section>

<footer class="wrap footer">
  <div class="col visit">
    <h4>Visit Our Shop</h4>
    <p>Lorem et ut sapien semper tempor diam elementum quis ullam corper nunc.</p>
  </div>
  <div class="col">
    <h4>Social Media</h4>
    <ul><li>Friendlane</li><li>Chirper</li><li>Clipstream</li><li>Circleplus</li></ul>
  </div>
  <div class="col">
    <h4>Our Services</h4>
    <ul><li>Curtains</li><li>Blinds</li><li>Fabrics</li><li>Sewing Supplies</li></ul>
  </div>
  <div class="col">
    <h4>Information</h4>
    <ul><li>About us</li><li>Opening Hours</li><li>Gallery</li><li>Newsletter</li></ul>
  </div>
  <div class="col contact">
    <h4>Contact us</h4>
    <ul><li>Tel: 00 000 0000</li><li>Email: info@velunor.nl</li><li>Maps Velunor</li></ul>
  </div>
</footer>

<div class="copyright">© Velunor. All Rights Reserved.</div>

</body>
</html>
```